Window and GutterCleaning Flyer A5 size double sided.

We need a double sided A5 flyer. Side 1, is for window cleaning, side 2 is for gutter cleaning. Licensed by Borough of Halvern Council.
Phone number 0800 315 4720.
Business address 7 Tarnlow Brae, North Pellin Edinburgh EH14 3RW.
www.clearpane-vista-services.com
We use a LoftPro Gutter inspection Cam to view your gutters first to see if they need doing.
Window cleaning ; Professional window cleaning services, what we offer, water fed pole window cleaning able to reach windows up to 60 feet.
Conservatory cleaning.
Conservatory roof cleaning.
Fascias & Soffits cleaning.
Excellent Customer Service.
Target Market(s)
domestic houses
Industry/Entity Type
window cleaning
Look and feel
Each slider illustrates characteristics of the customer's brand and the style your logo design should communicate.

```html
<!DOCTYPE html>
<html lang="en">
<head>
<meta charset="utf-8">
<title>ClearPane Vista – Window and Gutter Flyers</title>
<link rel="stylesheet" href="https://fonts.googleapis.com/css2?family=Bebas+Neue&family=Montserrat:wght@600;700;800&display=swap">
<style>
  :root{
    --navy:#2e2a6b;
    --ink:#111111;
    --paper:#f3f4f7;
    --paper-edge:#e4e6ec;
    --board:#959595;
    --leaf:#3b7a36;
    --white:#ffffff;
  }
  *{margin:0;padding:0;box-sizing:border-box}
  html,body{width:1200px;height:870px;overflow:hidden}
  body{background:var(--board);position:relative;font-family:'Bebas Neue',sans-serif;color:var(--ink)}
  .flyer{position:absolute;top:93px;width:483px;height:684px;overflow:hidden;
    background:linear-gradient(135deg,var(--white) 0%,var(--paper) 35%,var(--paper-edge) 50%,var(--paper) 65%,var(--white) 100%)}
  .flyer--window{left:90px}
  .flyer--gutter{left:626px}

  .brand{position:absolute;left:33px;top:40px;width:116px;color:var(--navy);font-family:'Bebas Neue',sans-serif;
    font-size:30px;line-height:.95;letter-spacing:1px;display:flex;align-items:center;gap:8px}
  .brand__mark{width:12px;height:12px;background:var(--navy);flex:none}

  .headline{position:absolute;left:33px;top:170px;font-size:60px;line-height:53px;color:var(--navy);letter-spacing:.5px}
  .headline .dark{color:var(--ink)}

  .photo{position:absolute;border-radius:50%;border:10px solid var(--navy);overflow:hidden}
  .photo--conservatory{left:196px;top:-98px;width:360px;height:360px;
    background:linear-gradient(160deg,#b5c8dc 0%,#e9eef2 40%,#a8553e 70%,#8b4a36 100%)}
  .photo--roof{left:246px;top:233px;width:248px;height:248px;
    background:linear-gradient(150deg,#a76b56 0%,#cfcfcf 35%,#8a8a76 60%,#b9bcc0 100%)}
  .photo--fascia{left:199px;top:-72px;width:340px;height:340px;
    background:linear-gradient(135deg,#f6f6f6 0%,#e9e9ea 50%,#bfc3c7 100%)}
  .photo--gutterpole{left:241px;top:232px;width:244px;height:244px;
    background:linear-gradient(140deg,#5f8a44 0%,#7ea65a 40%,#8c8f92 75%,#6b6e72 100%)}
  .photo span{display:none}

  .tag{position:absolute;background:var(--navy);color:var(--white);font-family:'Montserrat',sans-serif;font-weight:700;
    font-size:13px;letter-spacing:.5px;border-radius:14px;display:flex;align-items:center;justify-content:center}
  .tag--after{left:307px;top:407px;width:82px;height:24px}
  .tag--before{left:365px;top:439px;width:84px;height:23px}

  .price{position:absolute;border-radius:50%;background:var(--navy);color:var(--white);display:flex;flex-direction:column;align-items:center;justify-content:center;text-align:center}
  .price--window{left:290px;top:480px;width:172px;height:172px}
  .price--window .price__label{font-size:34px;line-height:30px}
  .price--window .price__amount{font-size:66px;line-height:60px}
  .price--gutter{left:224px;top:429px;width:118px;height:118px}
  .price--gutter .price__label{font-size:25px;line-height:22px}
  .price--gutter .price__amount{font-size:44px;line-height:40px}

  .services-band{position:absolute;left:0;width:184px;height:32px;background:var(--navy);color:var(--white);
    border-radius:0 16px 16px 0;font-size:28px;line-height:33px;padding-left:32px}
  .flyer--window .services-band{top:372px}
  .flyer--gutter .services-band{top:405px}

  .services{position:absolute;left:32px;list-style:none}
  .flyer--window .services{top:418px}
  .flyer--gutter .services{top:452px}
  .services li{display:flex;align-items:center;gap:6px;font-size:18px;line-height:20px;height:28.5px}
  .services svg{width:16px;height:16px;flex:none}

  .call{position:absolute;left:32px;top:574px;font-size:23px;line-height:24px}
  .phone{position:absolute;left:32px;top:598px;font-size:40px;line-height:40px;color:var(--navy)}
  .web{position:absolute;left:32px;top:640px;font-size:14px;line-height:14px}

  .arrow{position:absolute;height:auto}
  .arrow text{font-family:'Montserrat',sans-serif;font-weight:700;fill:var(--white)}

  .device{position:absolute;left:318px;top:510px;width:119px;height:92px;border-radius:8px;
    background:linear-gradient(160deg,#3a3f45 0%,#5b8fb8 45%,#2c2f33 100%)}
  .note{position:absolute;right:31px;top:609px;width:200px;text-align:right;font-family:'Montserrat',sans-serif;
    font-weight:700;font-size:9.5px;line-height:14px;color:var(--ink)}
</style>
</head>
<body>

<section class="flyer flyer--window">
  <div class="photo photo--conservatory" role="img" aria-label="Photo of a white uPVC conservatory against a brick house"></div>
  <div class="photo photo--roof" role="img" aria-label="Before and after photo of a conservatory roof being cleaned"></div>

  <div class="brand"><span class="brand__mark"></span><span>ClearPane Vista</span></div>

  <h1 class="headline">ClearPane<br><span class="dark">Vista</span><br>Cleaning</h1>

  <span class="tag tag--after">AFTER</span>
  <span class="tag tag--before">BEFORE</span>

  <div class="price price--window"><span class="price__label">Starting</span><span class="price__amount">$199</span></div>

  <h2 class="services-band">Our Services</h2>
  <ul class="services">
    <li><svg viewBox="0 0 16 16"><circle cx="8" cy="8" r="6.5" fill="none" stroke="#2e2a6b" stroke-width="1.8"/><path d="M4.5 8l2.5 2.5L15 2.5" fill="none" stroke="#2e2a6b" stroke-width="2" stroke-linecap="round"/></svg>Reach windows up to 60 feet</li>
    <li><svg viewBox="0 0 16 16"><circle cx="8" cy="8" r="6.5" fill="none" stroke="#2e2a6b" stroke-width="1.8"/><path d="M4.5 8l2.5 2.5L15 2.5" fill="none" stroke="#2e2a6b" stroke-width="2" stroke-linecap="round"/></svg>Conservatory cleaning</li>
    <li><svg viewBox="0 0 16 16"><circle cx="8" cy="8" r="6.5" fill="none" stroke="#2e2a6b" stroke-width="1.8"/><path d="M4.5 8l2.5 2.5L15 2.5" fill="none" stroke="#2e2a6b" stroke-width="2" stroke-linecap="round"/></svg>Conservatory roof cleaning</li>
    <li><svg viewBox="0 0 16 16"><circle cx="8" cy="8" r="6.5" fill="none" stroke="#2e2a6b" stroke-width="1.8"/><path d="M4.5 8l2.5 2.5L15 2.5" fill="none" stroke="#2e2a6b" stroke-width="2" stroke-linecap="round"/></svg>Fascias &amp; soffits cleaning</li>
  </ul>

  <p class="call">Call now today!</p>
  <p class="phone">0800 315 4720</p>
  <p class="web">WWW.CLEARPANE-VISTA-SERVICES.COM</p>
</section>

<section class="flyer flyer--gutter">
  <div class="photo photo--fascia" role="img" aria-label="Photo of a house roof edge showing gutter, fascia and soffit"></div>

  <svg class="arrow" style="left:313px;top:23px;width:148px" viewBox="0 0 148 58"><path d="M0 10H118V0L148 29L118 58V48H0L14 29Z" fill="#3b7a36"/><text x="70" y="38" font-size="22" text-anchor="middle">Gutter</text></svg>
  <svg class="arrow" style="left:267px;top:101px;width:149px" viewBox="0 0 149 58"><path d="M0 10H119V0L149 29L119 58V48H0L14 29Z" fill="#3b7a36"/><text x="68" y="38" font-size="22" text-anchor="middle">Fascia</text></svg>
  <svg class="arrow" style="left:244px;top:187px;width:133px" viewBox="0 0 133 51"><path d="M0 9H106V0L133 25L106 51V41H0Z" fill="#3b7a36"/><text x="50" y="34" font-size="21" text-anchor="middle">Soffit</text></svg>

  <div class="photo photo--gutterpole" role="img" aria-label="Photo of a gutter vacuum pole with inspection camera above a garden"></div>

  <div class="brand"><span class="brand__mark"></span><span>ClearPane Vista</span></div>

  <h1 class="headline" style="top:175px">Gutter<br>Repairing<br><span class="dark">And</span><br>Cleaning</h1>

  <div class="price price--gutter"><span class="price__label">Starting</span><span class="price__amount">$199</span></div>

  <h2 class="services-band">Our Services</h2>
  <ul class="services">
    <li><svg viewBox="0 0 16 16"><circle cx="8" cy="8" r="6.5" fill="none" stroke="#2e2a6b" stroke-width="1.8"/><path d="M4.5 8l2.5 2.5L15 2.5" fill="none" stroke="#2e2a6b" stroke-width="2" stroke-linecap="round"/></svg>Gutter cleaning</li>
    <li><svg viewBox="0 0 16 16"><circle cx="8" cy="8" r="6.5" fill="none" stroke="#2e2a6b" stroke-width="1.8"/><path d="M4.5 8l2.5 2.5L15 2.5" fill="none" stroke="#2e2a6b" stroke-width="2" stroke-linecap="round"/></svg>Down spouts</li>
    <li><svg viewBox="0 0 16 16"><circle cx="8" cy="8" r="6.5" fill="none" stroke="#2e2a6b" stroke-width="1.8"/><path d="M4.5 8l2.5 2.5L15 2.5" fill="none" stroke="#2e2a6b" stroke-width="2" stroke-linecap="round"/></svg>Gutter replacement</li>
    <li><svg viewBox="0 0 16 16"><circle cx="8" cy="8" r="6.5" fill="none" stroke="#2e2a6b" stroke-width="1.8"/><path d="M4.5 8l2.5 2.5L15 2.5" fill="none" stroke="#2e2a6b" stroke-width="2" stroke-linecap="round"/></svg>Gutter repair</li>
  </ul>

  <div class="device" role="img" aria-label="Gutter inspection camera monitor"></div>
  <p class="note">We use a LoftPro Gutter inspection Cam to view your gutters first to see if they need doing.</p>

  <p class="call">Call now today!</p>
  <p class="phone">0800 315 4720</p>
  <p class="web">WWW.CLEARPANE-VISTA-SERVICES.COM</p>
</section>

</body>
</html>
```